Insurance Pull Down Bar Ad

I need a simple magazine ad. At the top of the ad will read "Need Insurance? We Can Help." Below it will be a pull down bar that has been clicked on by a cursor. In the pull-down bar will be (one above the other) "medical, dental, life, disability, office-overhead, personal accident, travel, medical evacuation, critical illness and hospital indemnity."

In the attached file there is a logo in the upper left corner. It has our name and exclusively endorsed below it. Use this in the ad.

Colors should go with the logo attached.

We will need social media icons at the bottom: Palmora, Vidarro, Quipset, Careloft

I need it in a file that a graphic artist can edit.

Insurance

```html
<!DOCTYPE html>
<html lang="en">
<head>
<meta charset="utf-8">
<title>Need Insurance? We Can Help. – Magazine Ad</title>
<link rel="stylesheet" href="https://fonts.googleapis.com/css2?family=Questrial&family=Libre+Baskerville:ital@1&display=swap">
<style>
  :root {
    --backdrop: #5b5b5b;
    --page-top: #e6ecec;
    --page-mid: #c8d3d5;
    --page-bottom: #dde4e5;
    --brand-red: #b0203a;
    --brand-red-dark: #8e1329;
    --slate: #5d6d71;
    --slate-light: #7a8a8e;
    --rule: rgba(255,255,255,0.55);
    --white: #ffffff;
    --ink-grey: #5a5a5a;
  }
  * { box-sizing: border-box; margin: 0; padding: 0; }
  html, body { width: 1200px; height: 1000px; overflow: hidden; }
  body {
    background: var(--backdrop);
    font-family: "Questrial", "Century Gothic", sans-serif;
    position: relative;
  }
  .ad-page {
    position: absolute; left: 230px; top: 20px;
    width: 740px; height: 960px;
    background: radial-gradient(ellipse at 60% 40%, var(--page-top) 0%, var(--page-mid) 60%, var(--page-bottom) 100%);
  }
  .ad-frame {
    position: absolute; inset: 14px;
    border: 1.5px solid var(--brand-red);
    pointer-events: none;
  }
  .headline-bar {
    position: absolute; left: 70px; top: 128px;
    width: 600px; height: 46px;
    background: var(--white);
    border-radius: 12px 0 0 12px;
    box-shadow: 0 2px 4px rgba(0,0,0,0.2);
    display: flex; align-items: center;
  }
  .headline {
    padding-left: 34px;
    color: var(--brand-red);
    font-size: 27px; font-weight: 700;
    letter-spacing: 0.3px;
    -webkit-text-stroke: 0.6px var(--brand-red);
  }
  .dropdown-toggle {
    position: absolute; right: 0; top: -6px;
    width: 96px; height: 40px;
    background: var(--brand-red);
    border-radius: 8px 8px 8px 8px;
    display: flex; align-items: center; justify-content: center;
  }
  .menu-panel {
    position: absolute; left: 96px; top: 174px;
    width: 540px; height: 580px;
    background: linear-gradient(180deg, var(--slate-light) 0%, var(--slate) 100%);
    border-radius: 0 0 44px 44px;
    padding-top: 18px;
  }
  .menu-list { list-style: none; }
  .menu-item {
    position: relative;
    height: 52px;
    display: flex; align-items: center;
    padding-left: 30px;
    border-bottom: 1px solid var(--rule);
    color: var(--white);
    font-size: 30px;
    letter-spacing: 0.5px;
  }
  .menu-item:last-child { border-bottom: none; }
  .menu-item .item-marker {
    width: 26px; height: 26px; margin-right: 26px;
    background: var(--brand-red);
    border-radius: 3px;
    display: flex; align-items: center; justify-content: center;
    box-shadow: 0 1px 2px rgba(0,0,0,0.3);
  }
  .menu-item.is-selected {
    background: linear-gradient(180deg, #d0304b 0%, var(--brand-red) 55%, var(--brand-red-dark) 100%);
    margin-left: -26px; margin-right: -70px;
    padding-left: 56px;
    border-radius: 26px 6px 6px 26px;
    font-weight: 700;
    -webkit-text-stroke: 0.8px var(--white);
    border-bottom: none;
    box-shadow: 0 2px 5px rgba(0,0,0,0.35);
  }
  .menu-item.is-selected .item-marker { background: var(--white); }
  .pointer-cursor {
    position: absolute; right: 80px; top: 4px;
  }
  .social-links {
    position: absolute; right: 40px; top: 786px;
    display: flex; gap: 18px;
    list-style: none;
  }
  .social-link {
    display: flex; align-items: center; gap: 6px;
    font-size: 15px; color: var(--ink-grey);
  }
  .social-link .social-square {
    width: 14px; height: 14px; border-radius: 3px; background: var(--slate);
  }
  .brand-lockup {
    position: absolute; left: 46px; top: 836px;
  }
  .brand-name {
    display: flex; align-items: center; gap: 12px;
    color: var(--brand-red);
    font-size: 22px; line-height: 1.1;
    text-transform: uppercase;
    letter-spacing: 0.5px;
  }
  .brand-mark {
    width: 54px; height: 54px; background: var(--brand-red); flex: none;
  }
  .brand-endorsement {
    margin-top: 10px;
    font-family: "Libre Baskerville", Georgia, serif;
    font-style: italic;
    font-size: 15px;
    color: var(--ink-grey);
  }
</style>
</head>
<body>
  <section class="ad-page" aria-label="Insurance advertisement">
    <div class="ad-frame"></div>

    <div class="headline-bar">
      <h1 class="headline">“Need Insurance? We Can Help.”</h1>
      <div class="dropdown-toggle" aria-hidden="true">
        <svg width="22" height="14" viewBox="0 0 22 14"><path d="M2 2 L11 11 L20 2" fill="none" stroke="#fff" stroke-width="4" stroke-linecap="round" stroke-linejoin="round"/></svg>
      </div>
    </div>

    <nav class="menu-panel" aria-label="Insurance types">
      <ul class="menu-list">
        <li class="menu-item"><span class="item-marker"><svg width="10" height="12" viewBox="0 0 10 12"><path d="M2 1 L8 6 L2 11" fill="none" stroke="#fff" stroke-width="2.2"/></svg></span>Medical</li>
        <li class="menu-item"><span class="item-marker"><svg width="10" height="12" viewBox="0 0 10 12"><path d="M2 1 L8 6 L2 11" fill="none" stroke="#fff" stroke-width="2.2"/></svg></span>Dental</li>
        <li class="menu-item is-selected"><span class="item-marker"><svg width="10" height="12" viewBox="0 0 10 12"><path d="M2 1 L8 6 L2 11" fill="none" stroke="#333" stroke-width="2.2"/></svg></span>Life
          <svg class="pointer-cursor" width="34" height="40" viewBox="0 0 34 40" aria-hidden="true">
            <path d="M10 3 Q10 0 13 0 Q16 0 16 3 L16 16 L18 16 L18 13 Q18 11 20.5 11 Q23 11 23 13 L23 17 Q23 15 25.5 15 Q28 15 28 17 L28 19 Q28 17 30 17 Q32 17 32 19 L32 28 Q32 36 25 38 L15 38 Q10 37 7 32 L2 23 Q1 20 3.5 19.5 Q6 19 8 22 L10 25 Z" fill="#fff" stroke="#111" stroke-width="1.8" stroke-linejoin="round"/>
          </svg>
        </li>
        <li class="menu-item"><span class="item-marker"><svg width="10" height="12" viewBox="0 0 10 12"><path d="M2 1 L8 6 L2 11" fill="none" stroke="#fff" stroke-width="2.2"/></svg></span>Disability</li>
        <li class="menu-item"><span class="item-marker"><svg width="10" height="12" viewBox="0 0 10 12"><path d="M2 1 L8 6 L2 11" fill="none" stroke="#fff" stroke-width="2.2"/></svg></span>Office-overhead</li>
        <li class="menu-item"><span class="item-marker"><svg width="10" height="12" viewBox="0 0 10 12"><path d="M2 1 L8 6 L2 11" fill="none" stroke="#fff" stroke-width="2.2"/></svg></span>Personal accident</li>
        <li class="menu-item"><span class="item-marker"><svg width="10" height="12" viewBox="0 0 10 12"><path d="M2 1 L8 6 L2 11" fill="none" stroke="#fff" stroke-width="2.2"/></svg></span>Travel</li>
        <li class="menu-item"><span class="item-marker"><svg width="10" height="12" viewBox="0 0 10 12"><path d="M2 1 L8 6 L2 11" fill="none" stroke="#fff" stroke-width="2.2"/></svg></span>Medical evacuation</li>
        <li class="menu-item"><span class="item-marker"><svg width="10" height="12" viewBox="0 0 10 12"><path d="M2 1 L8 6 L2 11" fill="none" stroke="#fff" stroke-width="2.2"/></svg></span>Critical illness</li>
        <li class="menu-item"><span class="item-marker"><svg width="10" height="12" viewBox="0 0 10 12"><path d="M2 1 L8 6 L2 11" fill="none" stroke="#fff" stroke-width="2.2"/></svg></span>Hospital indemnity</li>
      </ul>
    </nav>

    <ul class="social-links" aria-label="Social media">
      <li class="social-link"><span class="social-square"></span>Palmora</li>
      <li class="social-link"><span class="social-square"></span>Vidarro</li>
      <li class="social-link"><span class="social-square"></span>Quipset</li>
      <li class="social-link"><span class="social-square"></span>Careloft</li>
    </ul>

    <footer class="brand-lockup">
      <div class="brand-name"><span class="brand-mark"></span><span>Lone Prairie Physicians<br>Insurance Trust</span></div>
      <p class="brand-endorsement">Exclusively endorsed by the Lone Prairie Physicians Society</p>
    </footer>
  </section>
</body>
</html>
```